The Iron Trials Borinquen Coast (ITBC) – Sponsorship Proposal 2026 | Second Edition

We are looking to redesign and elevate our Sponsorship Proposal for the second edition of The Iron Trials Borinquen Coast (ITBC) - a Tactical Fitness competition that combines functional fitness and live-fire shooting in a safe and controlled environment.
The first edition (March 7, 2026) was a proven success, and the updated proposal must reflect that evolution from concept to validated event.
OBJECTIVE
Create a visually striking, premium, and highly structured sponsorship proposal that communicates:
- Credibility (proven event)
- Growth (scaling momentum)
- Experience (not just competition, but a full event)
----------------------------
KEY DATA TO INCLUDE (VERY IMPORTANT)
The design must highlight the following real metrics prominently:
- 96 registered athletes
- 240+ spectators
- 35 volunteers
- 370+ total attendees
- 14 female athletes
- 5 youth participants (ages 12–16)
- $3,300 awarded in prize money
INAUGURAL SPONSORS:
- Coastal Sky Corps
- Caribe Territorial Defense Reserve
- Harbor Militia Auxiliary
- Crestmoor Real Estate
- MTK (Mariposa Trek Kit)
- Quillstone Studio
- Reef Motion 442, KORVA San Juan
- Premier Dispatch PR
- Core Harmony
NEXT EVENT (IMPORTANT FOR DESIGN STORY)
- Event Date: December 19, 2026
- Expected Attendance:
- 130+ athletes
- 300+ spectators
- ~500 total attendees
- Theme: Christmas Experience
- Full event decorated in Christmas theme
- Food vendors + traditional Puerto Rican roasted pork (150+ lbs), community, and sponsor activations
👉 This is NOT just a competition - it is an experience-driven event.
STRUCTURE (BASED ON CURRENT PROPOSAL)
- Use the existing proposal as structural reference , but improve layout, hierarchy, and storytelling:
- Cover Page (modern + bold)
- Executive Summary (UPDATED with real results)
- Event Concept / Experience
- Audience & Attendance (with real + projected numbers)
- Sponsors (social proof section)
- Sponsorship Packages (Alpha = $10,000, Bravo = $1,000, Charlie = $500, Delta = $250)
- Why Sponsor ITBC
- Contact Page
EVENT DIVISIONS (UPDATED – VERY IMPORTANT)
The proposal must clearly showcase the five official competition divisions, with strong visual hierarchy (icons, images, or cards per division). This section should feel dynamic, premium, and easy to scan.
Divisions to include:
SCALE DIVISION (Adaptive)
An adaptive division for those who want to experience ITBC in a controlled environment.
No rankings. No prizes.
This is about completing the challenge.
BEGINNER DIVISION
For athletes ready to compete in a structured and approachable format.
Challenging, but accessible.
Athletes compete for placement.
INTERMEDIATE DIVISION
For athletes with a strong foundation in fitness and shooting.
Heavier loads. Higher standards.
Performance matters.
JÍBARO DIVISION (Elite)
The highest level of competition at ITBC.
Retention holsters required. Rifles carried in slings. Heavier loads.
Built for athletes who want to prove themselves.
MASTERS 45+ DIVISION
For athletes 45+ who want to compete while prioritizing longevity and control.
Maintains competitive intensity within an age-based category.
2-GUN FORMAT (IMPORTANT – INCLUDE BELOW DIVISIONS)
All divisions are available in either:
Pistol
2-Gun (Pistol + Rifle)
In the 2-Gun format, athletes utilize both pistol and rifle throughout the competition, transitioning between weapons under physical fatigue and time pressure.
DESIGN NOTE FOR THIS SECTION
Present divisions as individual visual blocks/cards (like the reference provided)
Use bold titles + short descriptions (keep text tight)
Include action images per division if possible
Highlight Jíbaro Division as the elite tier visually
Ensure this section is one of the most visually engaging pages in the proposal
DESIGN STYLE & VISUAL DIRECTION
We want a military / tactical / premium fitness aesthetic, similar to brands like:
- Brindle Athletics
- The Valor Circuit
- MeshLift-style event decks
Tone:
- Strong
- Clean
- Masculine but modern
- Minimal clutter
COLOR PALETTE (MANDATORY)
Use the following brand colors:
- Light Olive Green (#636B2F)
- Dark Olive Green (#3D4127)
- Sand / Khaki (#C2B280)
- Charcoal / Black (#1C1C1C)
- Light Gray (#D3D3D3)
- White (#FFFFFF)
- Accent Red (#C80018) – for highlights only
DESIGN NOTES
- Use bold typography (military/tactical feel - I will include the font called BOOTCAMP which is the main font used for the first edition)
- Strong use of contrast (dark backgrounds + light text)
- Icons for stats (athletes, spectators, etc.)
- Clean infographics for numbers
- Full-page images for impact (action shots, athletes, shooting, fitness)
- Official logo included (PNG and vectorized)
- Keep it visually dynamic but easy to read
IMPORTANT MESSAGE SHIFT
The proposal must clearly communicate:
- This is NOT a new event
- This is a proven concept that is scaling
Before: “Support us”
Now: “Join a growing movement early”
FINAL DELIVERABLE
- Print-ready PDF (high quality)
- Editable source file (Illustrator)
- Modern, clean layout with strong visual hierarchy
Website: www.theitbc-example.com
Instagram: https://www.instagram.com/theitbc_demo/
- BOOTCAMP

```html
<!DOCTYPE html>
<html lang="en">
<head>
<meta charset="utf-8">
<title>ITBC Sponsorship Proposal 2026</title>
<link href="https://fonts.googleapis.com/css2?family=Staatliches&family=Open+Sans:wght@400;600;700&display=swap" rel="stylesheet">
<style>
:root{
  --olive:#636B2F;
  --olive-dark:#3D4127;
  --sand:#C2B280;
  --charcoal:#1C1C1C;
  --char-2:#262624;
  --gray:#D3D3D3;
  --white:#FFFFFF;
  --sheet:#A9A9A9;
  --head:"Staatliches", Impact, sans-serif;
  --body:"Open Sans", Arial, sans-serif;
}
*{margin:0;padding:0;box-sizing:border-box}
html,body{width:1200px;height:4369px;overflow:hidden}
body{background:var(--sheet);position:relative;font-family:var(--body);color:var(--gray)}
.page{position:absolute;width:528px;height:682px;overflow:hidden;background:radial-gradient(ellipse 70% 55% at 68% 62%,#2a2a28 0%,#222220 45%,var(--charcoal) 80%)}
.abs{position:absolute}

/* photo areas: layered tones of the scene */
.photo{position:absolute;background:
  radial-gradient(ellipse 22% 40% at 45% 70%,rgba(22,22,20,.85) 0 55%,transparent 70%),
  radial-gradient(ellipse 50% 30% at 70% 20%,rgba(205,198,170,.35),transparent 70%),
  linear-gradient(180deg,#5d6a3a 0%,#6a6852 38%,#4a4940 65%,#242422 100%)}
.photo.range{background:
  radial-gradient(ellipse 14% 34% at 22% 40%,rgba(18,18,18,.9) 0 55%,transparent 70%),
  radial-gradient(ellipse 12% 30% at 52% 48%,rgba(28,28,26,.85) 0 55%,transparent 70%),
  radial-gradient(ellipse 16% 10% at 62% 38%,rgba(150,140,120,.5),transparent 70%),
  radial-gradient(ellipse 60% 25% at 75% 12%,rgba(150,170,110,.45),transparent 70%),
  linear-gradient(180deg,#4f6132 0%,#5f6846 22%,#7a7664 45%,#4c4b42 68%,#1c1c1c 92%)}
.photo.aerial{background:
  repeating-radial-gradient(circle at 50% 70%,rgba(30,30,28,.25) 0 3px,rgba(120,118,100,.18) 3px 6px),
  linear-gradient(180deg,#3f5a2a 0%,#56703a 20%,#e6e6e0 22%,#d8d8d0 26%,#4c5a36 27%,#5a5b50 45%,#505048 75%,#3e3d36 100%)}
.photo.portrait{background:
  radial-gradient(ellipse 35% 55% at 50% 62%,rgba(24,24,24,.92) 0 60%,transparent 72%),
  radial-gradient(ellipse 14% 8% at 50% 20%,rgba(60,160,180,.35),transparent 70%),
  linear-gradient(180deg,#627044 0%,#7c7a62 30%,#8a8470 50%,#4a473e 85%,#2a2926 100%)}
.photo.shooter{background:
  radial-gradient(ellipse 30% 50% at 40% 68%,rgba(30,30,28,.95) 0 60%,transparent 72%),
  radial-gradient(ellipse 35% 8% at 72% 38%,rgba(60,60,56,.7),transparent 70%),
  linear-gradient(90deg,#5c6c36 0%,#4d5632 35%,#343430 70%,#1c1c1c 100%)}
.photo.shirt{background:
  radial-gradient(ellipse 25% 8% at 52% 40%,rgba(194,178,128,.55),transparent 70%),
  radial-gradient(ellipse 20% 6% at 52% 52%,rgba(194,178,128,.4),transparent 70%),
  radial-gradient(ellipse 35% 25% at 25% 22%,rgba(140,140,130,.5),transparent 70%),
  linear-gradient(160deg,#5c5d52,#3a3a35 55%,#2a2a27)}

.ghost-num{position:absolute;left:-6px;top:-14px;font-family:var(--head);font-size:120px;color:rgba(255,255,255,.06);line-height:1}
.title{position:absolute;font-family:var(--head);color:var(--sand);font-size:31px;line-height:.95;letter-spacing:1px}
.tag{position:absolute;font-size:7px;color:var(--gray);opacity:.8}
.side{position:absolute;right:10px;top:60px;writing-mode:vertical-rl;font-size:6px;letter-spacing:1px;color:var(--gray);opacity:.7}
.txt{position:absolute;font-size:6.2px;line-height:1.45;color:var(--gray)}
.txt p{margin-bottom:6px}
.circ{position:absolute;border-radius:50%;border:3px solid var(--sand);background:
  radial-gradient(ellipse 24% 40% at 50% 68%,rgba(26,26,24,.9) 0 55%,transparent 70%),
  radial-gradient(ellipse 60% 30% at 50% 15%,rgba(150,165,110,.5),transparent 70%),
  linear-gradient(180deg,#5f6b3d 0%,#8a8468 45%,#5a564a 75%,#34332d 100%)}
.circ.alt{background:
  radial-gradient(ellipse 28% 42% at 42% 66%,rgba(120,40,40,.55) 0 50%,transparent 68%),
  radial-gradient(ellipse 60% 30% at 50% 12%,rgba(170,180,130,.5),transparent 70%),
  linear-gradient(180deg,#6b7346 0%,#8e8a70 45%,#5c584b 78%,#34332d 100%)}
.h-sm{font-family:var(--head);color:var(--sand);font-size:17px;line-height:1}
.logo-badge{position:absolute;border-radius:50%;background:var(--charcoal);border:3px solid var(--white);display:flex;align-items:center;justify-content:center;font-family:var(--head);color:var(--white);letter-spacing:2px;box-shadow:0 0 0 8px var(--charcoal)}

/* cover */
.cover-title{left:30px;top:392px;font-family:var(--head);color:var(--white);font-size:42px;line-height:1.02}
.band{position:absolute;background:var(--olive);color:var(--white);font-weight:700;font-size:14px;display:flex;align-items:center;padding-left:30px;clip-path:polygon(0 0,100% 0,88% 100%,0 100%)}
.cover-meta{position:absolute;font-size:9px;color:var(--white);text-align:right;line-height:1.35;white-space:nowrap}

/* exec */
.div-band{position:absolute;left:39px;top:324px;width:489px;height:152px;background:var(--olive)}
.div-col{position:absolute;top:12px;width:150px}
.div-col .h-sm{color:var(--white);display:flex;align-items:center;gap:5px}
.div-col .h-sm:before{content:"";width:7px;height:7px;background:var(--sand)}
.div-col p{font-size:6px;line-height:1.45;color:var(--gray);margin-top:6px}

/* audience */
.stat{position:absolute;width:90px;text-align:center;transform:translateX(-45px)}
.stat .ic{width:46px;height:46px;margin:0 auto;border-radius:50%;background:var(--olive-dark);border:2px solid var(--sand);display:flex;align-items:center;justify-content:center}
.stat .lbl{margin-top:8px;font-family:var(--head);font-size:12px;color:var(--white);line-height:1.05}
.prize{position:absolute;width:102px;height:102px;border-radius:50%;background:var(--olive);display:flex;flex-direction:column;align-items:center;justify-content:center;color:var(--white)}
.prize b{font-family:var(--head);font-size:28px;font-weight:400;line-height:1}
.prize span{font-size:7px;text-align:center;line-height:1.2}

/* sponsors */
.marks{position:absolute;left:286px;top:555px;width:220px;display:flex;flex-wrap:wrap;gap:8px 12px;align-items:center}
.mark{font-size:6.5px;font-weight:700;color:var(--gray);display:flex;align-items:center;gap:3px}
.mark i{width:8px;height:8px;border-radius:50%;background:var(--gray);display:block}

/* packages */
.pkg-alpha{position:absolute;left:22px;top:137px;width:470px;height:153px;background:var(--olive);border:2px solid var(--olive-dark);padding:12px 14px 0 14px}
.pkg-alpha h3,.pkg h3{font-family:var(--head);font-weight:400;color:var(--white);line-height:1}
.pkg-alpha h3{font-size:20px}
.pill{display:inline-block;background:var(--sand);color:var(--charcoal);font-size:5px;font-weight:700;padding:1px 6px;margin:5px 0 4px}
.pkg-alpha ul,.pkg ul{list-style:none;font-size:5.6px;line-height:1.45;color:var(--gray)}
.cols2{columns:2;column-gap:16px}
.pkg{position:absolute;top:298px;width:127px;height:260px;background:var(--char-2);border:2px solid var(--olive);padding:10px 8px}
.pkg h3{font-size:13px}
.pkg h3 .price{font-size:17px;color:var(--sand)}
.pkg .sub{font-size:5.6px;margin-top:4px;line-height:1.4}
.chev{display:block;margin-bottom:4px}
.inkind{position:absolute;left:39px;top:570px;width:431px;height:93px;background:var(--sand);padding:12px 12px 12px 44px;color:var(--charcoal)}
.inkind h3{font-family:var(--head);font-weight:400;font-size:17px;line-height:1}
.inkind p{font-size:6px;margin-top:3px}
.inkind ul{list-style:none;font-size:5.6px;columns:2;margin-top:2px}
.inkind .pill{background:var(--olive);color:var(--white)}

/* divisions */
.dv{position:absolute;width:140px;text-align:center;transform:translateX(-70px)}
.dv .circ{position:relative;width:102px;height:102px;margin:0 auto}
.dv .badge{position:absolute;right:0;top:0;width:22px;height:22px;border-radius:50%;background:var(--gray);border:2px solid var(--charcoal)}
.dv h4{font-family:var(--head);font-weight:400;font-size:11px;color:var(--sand);margin-top:10px;line-height:1.05}
.dv .kind{font-size:5.5px;opacity:.7;margin-top:1px}
.dv p{font-size:6.2px;line-height:1.45;margin-top:12px;color:var(--gray)}
.jibaro{position:absolute;left:19px;top:351px;width:169px;height:271px;background:var(--sand)}
.dv.elite h4{color:var(--charcoal);font-size:13px}
.dv.elite p,.dv.elite .kind{color:var(--charcoal)}

/* expected */
.exp{position:absolute;right:36px;text-align:right;color:var(--white)}
.exp h3{font-family:var(--head);font-weight:400;color:var(--sand);font-size:22px;line-height:1.05}
.exp ul{list-style:none;font-size:8px;line-height:1.6}
</style>
</head>
<body>

<!-- COVER -->
<section class="page cover" style="left:620px;top:64px">
  <div class="photo range" style="left:0;top:0;width:528px;height:440px" role="img" aria-label="Athletes in ear protection firing pistols on an outdoor range"></div>
  <svg class="abs" style="left:0;top:0" width="528" height="682" viewBox="0 0 528 682" aria-hidden="true">
    <path d="M0 380 L0 682 L528 682 L528 300 C500 300 470 340 433 356 A163 163 0 0 1 107 356 C80 360 40 372 0 380Z" fill="#1C1C1C"/>
    <circle cx="270" cy="356" r="163" fill="none" stroke="#1C1C1C" stroke-width="26"/>
  </svg>
  <div class="logo-badge" style="left:188px;top:274px;width:164px;height:164px;font-size:30px">ITBC</div>
  <div class="photo portrait" style="left:360px;top:410px;width:120px;height:120px;border-radius:50%" role="img" aria-label="Athlete wearing ear protection and glasses"></div>
  <h1 class="abs cover-title">THE IRON TRIALS<br>BORINQUEN COAST<br>(ITBC)</h1>
  <div class="band" style="left:0;top:554px;width:300px;height:43px">SPONSORSHIP PROPOSAL</div>
  <div class="cover-meta" style="right:30px;top:528px;font-weight:600">PREPARED BY:<br>RAFAEL M. ORTEGA,<br>FOUNDER &amp; CEO</div>
  <div class="cover-meta" style="right:30px;top:590px;font-size:6px">Ridgeline Range Club<br>Cerro Alto,<br>Puerto Rico</div>
  <div class="cover-meta" style="left:60px;top:623px;text-align:center;width:200px">EVENT DATE:<br>DECEMBER 19, 2026 | 7:30AM - 5:00PM</div>
  <div class="cover-meta" style="right:30px;top:640px;font-size:6px">Email: rafael@theitbc-example.com | Phone: 555-014-0199</div>
  <div class="cover-meta" style="right:30px;top:656px;font-size:8px">www.instagram.com/theitbc_demo</div>
</section>

<!-- EXECUTIVE SUMMARY -->
<section class="page exec" style="left:83px;top:781px">
  <div class="ghost-num">01</div>
  <h2 class="title" style="left:44px;top:41px">1. EXECUTIVE<br>SUMMARY</h2>
  <div class="tag" style="right:30px;top:38px">[Company Profile]</div>
  <div class="txt" style="left:44px;top:122px;width:440px">The ITBC is the 1st functional fitness and live-fire competition in the entire Caribbean - a one-of-a-kind event where strength, precision, and adrenaline meet. In a single day, athletes, shooters, and enthusiasts from both worlds will test their endurance, focus, and competitive spirit in a course designed to challenge both physical and mental limits.</div>
  <div class="circ" style="left:83px;top:168px;width:102px;height:102px" role="img" aria-label="Athlete on the shooting course"></div>
  <div class="circ alt" style="left:225px;top:168px;width:102px;height:102px" role="img" aria-label="Female athlete carrying weight"></div>
  <div class="circ" style="left:369px;top:168px;width:102px;height:102px" role="img" aria-label="Athlete aiming a pistol"></div>
  <div class="div-band">
    <div class="div-col" style="left:12px"><div class="h-sm">SCALE</div><p>Designed for first-time competitors and athletes new to tactical tests or shooting sports. Movements, loads, and shooting distances are intentionally reduced, with an emphasis on safety, fundamentals, and confidence-building. This division prioritizes learning, controlled execution, and a positive competitive experience.</p></div>
    <div class="div-col" style="left:181px"><div class="h-sm">BEGINNER</div><p>Ideal for athletes with some fitness experience and basic weapons handling who are ready to be challenged. Movements and shooting distances increase compared to Scale, while still maintaining approachable standards. This division rewards consistency, composure, and proper execution under moderate physical and mental stress.</p></div>
    <div class="div-col" style="left:325px"><div class="h-sm">INTERMEDIATE</div><p>Built for experienced athletes comfortable with functional tests and weapons handling under pressure. Expect higher physical demands, longer shooting distances, and more complex problem-solving. This division tests conditioning, accuracy, and decision-making while maintaining strict safety and equipment standards.</p></div>
  </div>
  <div class="txt" style="left:44px;top:546px;width:200px">The 2-Gun option is available in Scale, Beginner, and Intermediate divisions. Athletes competing in 2-Gun will use both a pistol and a rifle during designated stages. Rifle use is integrated in a controlled manner appropriate to each division's difficulty level, with distances and complexity scaled accordingly. All 2-Gun athletes must bring their own rifle and comply with all safety, equipment, and range requirements.</div>
  <div class="txt" style="left:262px;top:546px;width:150px">More than just a competition, the ITBC will be an immersive experience where fitness and marksmanship converge with Puerto Rican pride. Participants will run, carry, drag, and shoot under the watchful eye of certified Range Officers, in a safe and controlled environment, with live music, commentators, and an energetic audience.</div>
  <svg class="abs" style="left:420px;top:520px" width="80" height="110" viewBox="0 0 80 110" aria-hidden="true">
    <g fill="none" stroke="#3a3a36" stroke-width="10">
      <polyline points="5,15 40,35 75,15"/><polyline points="5,40 40,60 75,40"/><polyline points="5,65 40,85 75,65"/><polyline points="5,90 40,110 75,90"/>
    </g>
  </svg>
</section>

<!-- EVENT CONCEPT -->
<section class="page concept" style="left:619px;top:781px">
  <div class="ghost-num">02</div>
  <h2 class="title" style="left:39px;top:41px">2. EVENT CONCEPT /<br>EXPERIENCE</h2>
  <div class="side">SPONSORSHIP PROPOSAL &nbsp; | &nbsp; 3</div>
  <div class="txt" style="left:39px;top:122px;width:440px">
    <p>Ridgeline Range Club, Cerro Alto, Puerto Rico. The club spans 172 acres, earning exclusive use of the grounds for The Iron Trials Borinquen Coast. The event will occupy the newly leveled site (~90m x 20m) and surrounding trails for running track stages, creating a safe and controlled setting for both physical and shooting challenges.</p>
    <p>The 2-Gun option is available in Scale, Beginner, and Intermediate divisions. Athletes competing in 2-Gun will use both a pistol and a rifle during designated stages. Rifle use is integrated in a controlled manner appropriate to each division's difficulty level, with distances and complexity scaled accordingly.</p>
  </div>
  <div class="photo shooter" style="left:0;top:200px;width:330px;height:482px" role="img" aria-label="Female athlete with ear protection aiming a pistol"></div>
  <div class="abs" style="left:0;top:324px;width:200px;height:152px;background:rgba(99,107,47,.75)"></div>
  <div class="txt" style="left:190px;top:225px;width:150px">The 2-Gun option is available in Scale, Beginner, and Intermediate divisions. Athletes competing in 2-Gun will use both a pistol and a rifle during designated stages. Rifle use is integrated in a controlled manner appropriate to each division's difficulty level, with distances and complexity scaled accordingly. All 2-Gun athletes must bring their own rifle and comply with all safety, equipment, and range requirements.</div>
  <div class="txt" style="left:215px;top:455px;width:220px">
    <p>The 2-Gun option is available in Scale, Beginner, and Intermediate divisions. Athletes competing in 2-Gun will use both a pistol and a rifle during designated stages. Rifle use is integrated in a controlled manner appropriate to each division's difficulty level, with distances and complexity scaled accordingly.</p>
    <p>The 2-Gun option is available in Scale, Beginner, and Intermediate divisions. Athletes competing in 2-Gun will use both a pistol and a rifle during designated stages. All 2-Gun athletes must bring their own rifle and comply with all safety, equipment, and range requirements.</p>
  </div>
</section>

<!-- AUDIENCE -->
<section class="page audience" style="left:83px;top:1492px">
  <div class="ghost-num">03</div>
  <h2 class="title" style="left:40px;top:41px">3. AUDIENCE<br>&amp; ATTENDANCE</h2>
  <div class="tag" style="left:330px;top:38px">[2026/18]</div>
  <div class="abs" style="left:12px;top:150px;writing-mode:vertical-rl;transform:rotate(180deg);font-size:6px;opacity:.7">COMPANY PROFILE &nbsp; | &nbsp; 4</div>
  <div class="photo aerial" style="left:397px;top:0;width:131px;height:682px" role="img" aria-label="Aerial view of the crowd and tents at the event"></div>

  <div class="stat" style="left:95px;top:163px"><div class="ic"><svg width="24" height="24" viewBox="0 0 24 24"><circle cx="12" cy="8" r="4" fill="#C2B280"/><path d="M4 21c0-5 4-7 8-7s8 2 8 7z" fill="#C2B280"/></svg></div><div class="lbl">96 REGISTERED<br>ATHLETES</div></div>
  <div class="stat" style="left:185px;top:163px"><div class="ic"><svg width="26" height="24" viewBox="0 0 26 24"><circle cx="7" cy="9" r="3" fill="#C2B280"/><circle cx="13" cy="7" r="3.5" fill="#C2B280"/><circle cx="19" cy="9" r="3" fill="#C2B280"/><path d="M2 20c0-4 3-6 5-6h12c2 0 5 2 5 6z" fill="#C2B280"/></svg></div><div class="lbl">240+<br>SPECTATORS</div></div>
  <div class="stat" style="left:281px;top:163px"><div class="ic"><svg width="24" height="24" viewBox="0 0 24 24"><path d="M12 3l2.6 5.6 6 .6-4.5 4 1.3 6-5.4-3.1-5.4 3.1 1.3-6-4.5-4 6-.6z" fill="#C2B280"/></svg></div><div class="lbl">35<br>VOLUNTEERS</div></div>
  <div class="stat" style="left:95px;top:285px"><div class="ic"><svg width="24" height="24" viewBox="0 0 24 24"><rect x="4" y="5" width="16" height="15" rx="2" fill="none" stroke="#C2B280" stroke-width="2"/><path d="M4 10h16" stroke="#C2B280" stroke-width="2"/></svg></div><div class="lbl">370+ TOTAL<br>ATTENDEES</div></div>
  <div class="stat" style="left:185px;top:285px"><div class="ic"><svg width="24" height="24" viewBox="0 0 24 24"><circle cx="12" cy="8" r="4.5" fill="#C2B280"/><path d="M5 21l2-6h10l2 6z" fill="#C2B280"/></svg></div><div class="lbl">14<br>FEMALE ATHLETES</div></div>
  <div class="stat" style="left:281px;top:285px"><div class="ic"><svg width="24" height="24" viewBox="0 0 24 24"><circle cx="12" cy="9" r="3.5" fill="#C2B280"/><path d="M6 21c0-4 3-6 6-6s6 2 6 6z" fill="#C2B280"/></svg></div><div class="lbl">5 YOUTH<br>PARTICIPANTS<br>(AGES 12-16)</div></div>

  <div class="txt" style="left:64px;top:415px;width:150px">
    <p>Our audience is made up of active adults who train, compete, and spend on gear, nutrition, and services that support their lifestyle. Many come with family and friends for the full day.</p>
    <p>Spectators stay from morning to close, visiting sponsor tables, food vendors, and the competition area between heats.</p>
  </div>
  <div class="txt" style="left:232px;top:415px;width:150px">Athletes travel from across the island to compete. The first edition drew a strong mix of veterans, first responders, gym members, and new shooters eager to test themselves in a safe format with certified officers and a clear set of rules for everyone.</div>
</section>

<!-- AUDIENCE (continued) -->
<section class="page audience-2" style="left:619px;top:1492px">
  <div class="photo aerial" style="left:0;top:0;width:212px;height:682px" role="img" aria-label="Aerial view of athletes and spectators gathered around the event tents"></div>
  <div class="abs" style="left:161px;top:44px;width:322px;height:5px;background:var(--sand)"></div>
  <div class="side">SPONSORSHIP PROPOSAL &nbsp; | &nbsp; 5</div>
  <div class="prize" style="left:156px;top:483px"><b>$3,300</b><span>awarded in prize<br>money</span></div>
  <div class="txt" style="left:249px;top:110px;width:217px">
    <p>Strong turnout: the first edition filled every heat and the stands stayed full through the final awards.</p>
    <p>Our athletes are loyal. Most have already asked about the next date and plan to bring a training partner.</p>
    <p>Sponsor visibility lasts all day, from check-in and the briefing to each stage and the podium photos.</p>
    <p>Families return. Spectators came back for the awards and shared the event widely on social media.</p>
    <p>Growth is steady. We project more athletes, more spectators, and a bigger village for partners this year.</p>
    <p>Community matters. Local vendors, volunteers, and range staff make the day feel like a true island gathering.</p>
    <p>Safety first. Certified officers oversee every stage so sponsors can join a well run and trusted event.</p>
  </div>
</section>

<!-- SPONSORS -->
<section class="page sponsors" style="left:83px;top:2202px">
  <div class="ghost-num">04</div>
  <h2 class="title" style="left:56px;top:52px">4. SPONSORS</h2>
  <div class="tag" style="right:30px;top:30px">Second Edition</div>
  <div class="txt" style="left:56px;top:86px;width:440px">
    <p>The Iron Trials Borinquen Coast (ITBC) attracts a highly concentrated audience of active, motivated adults with strong purchasing power and high brand loyalty to companies that support their performance-driven lifestyle. Estimated attendance is 260–300 people, including 70+ athletes, 150 spectators, and 20+ staff and volunteers.<br>AVAILABLE SPACE<br>SPONSOR TABLE<br>CHECK-IN AREA<br>SPONSORSHIP VILLAGE</p>
    <p>The core demographic is ages 25–44, with additional participation from 18–24 and 45–55, and consists largely of mid- to high-income professionals working in technology, engineering, construction, healthcare, emergency services, law enforcement, military, security.</p>
  </div>
  <div class="photo shirt" style="left:-92px;top:247px;width:390px;height:390px;border-radius:50%" role="img" aria-label="Athlete in ear protection wearing a sponsor shirt"></div>
  <div class="txt" style="left:150px;top:214px;width:160px">The audience regularly invests in gym memberships, coaching, supplements, outdoor and tactical gear, events, and training, and is known for high brand loyalty and early adoption of performance equipment, tactical apparel, and new technology - making ITBC an ideal platform for sponsors seeking direct engagement with disciplined, ambitious consumers. First responders, veterans, and all live-fire stages will be supervised at all times by certified Range Officers to ensure the highest safety standards throughout the event.</div>
  <div class="txt" style="left:361px;top:214px;width:150px">Event week schedule: Friday - final setup, equipment transport and range safety check. Saturday - athlete check-in at 6:30 AM, followed by the safety briefing and competition from 7:30 AM to 5:00 PM, concluding with the awards ceremony. Sunday - teardown and site wrap-up. Sponsors may set up on Friday afternoon and remain through the awards, with access to athletes, families, and spectators during every heat.</div>
  <div class="marks">
    <span class="mark"><i></i>Coastal Sky Corps</span>
    <span class="mark"><i></i>Caribe Territorial Defense Reserve</span>
    <span class="mark"><i></i>Harbor Militia Auxiliary</span>
    <span class="mark"><i></i>Crestmoor Real Estate</span>
    <span class="mark"><i></i>MTK</span>
    <span class="mark"><i></i>Quillstone Studio</span>
    <span class="mark"><i></i>Reef Motion 442</span>
    <span class="mark"><i></i>KORVA San Juan</span>
    <span class="mark"><i></i>Premier Dispatch PR</span>
    <span class="mark"><i></i>Core Harmony</span>
  </div>
</section>

<!-- SPONSORSHIP OPPORTUNITIES -->
<section class="page packages" style="left:619px;top:2202px">
  <div class="ghost-num">05</div>
  <div class="abs" style="left:290px;top:32px;width:180px;height:70px;border-radius:35px;background:#2a2a28" role="img" aria-label="Faint military star insignia decoration"></div>
  <h2 class="title" style="left:34px;top:36px">5. SPONSORSHIP<br>OPPORTUNITIES</h2>
  <div class="side">SPONSORSHIP PROPOSAL &nbsp; | &nbsp; 7</div>
  <div class="pkg-alpha">
    <h3>ALPHA SPONSOR – $10,000 (MAIN SPONSOR – 1 AVAILABLE)</h3>
    <div style="font-size:6px;color:var(--white);margin-top:3px">The premier sponsorship tier. Full brand integration across the entire event, including naming presence in key locations and all major advertising.</div>
    <span class="pill">INCLUDES</span>
    <ul class="cols2">
      <li>• Recognition as "The ITBC Presented by [Company Name]" in all promotional and press materials.</li>
      <li>• Prominent logo on shirts, banners, signage, and digital platforms.</li>
      <li>• Opportunity for opening ceremony remarks.</li>
      <li>• Exclusive 20 x 20 booth space for brand activation.</li>
      <li>• Co-branding on trophies, athlete wristbands, and backdrops.</li>
      <li>• Featured presence in social media campaigns and post-event recap video.</li>
      <li>• Priority reveal rights for future editions.</li>
      <li>• Option to display vehicles, large equipment, or installations onsite.</li>
      <li>• Inclusion of promotional materials in athlete bags.</li>
      <li>• Three complimentary athlete entries.</li>
    </ul>
  </div>
  <div class="pkg" style="left:42px">
    <svg class="chev" width="20" height="16" viewBox="0 0 20 16"><g fill="none" stroke="#D3D3D3" stroke-width="3"><polyline points="2,2 10,7 18,2"/><polyline points="2,8 10,13 18,8"/></g></svg>
    <h3>BRAVO SPONSOR<br><span class="price">$1,000</span><br>(UP TO 3 AVAILABLE)</h3>
    <div class="sub">Offers solid brand visibility and opportunities for active participation.</div>
    <span class="pill">INCLUDES</span>
    <ul><li>• Logo on athlete shirts</li><li>• Logo on event banner</li><li>• Two social media posts</li><li>• Space for branded tent</li><li>• Recognition on media and web</li><li>• Inclusion in event video and photos</li><li>• Promo materials in athlete bags</li><li>• Option to sponsor a stage</li><li>• Two complimentary athlete entries</li></ul>
  </div>
  <div class="pkg" style="left:188px">
    <svg class="chev" width="20" height="16" viewBox="0 0 20 16"><g fill="none" stroke="#D3D3D3" stroke-width="3"><polyline points="2,2 10,7 18,2"/><polyline points="2,8 10,13 18,8"/></g></svg>
    <h3>CHARLIE SPONSOR<br><span class="price">$500</span><br>(UP TO 20 AVAILABLE)</h3>
    <div class="sub">Designed for brands seeking event presence and digital promotion at an accessible level.</div>
    <span class="pill">INCLUDES</span>
    <ul><li>• Logo on athlete shirts</li><li>• Logo on event banner</li><li>• One social media post</li><li>• Recognition on media and web</li><li>• Inclusion in event recap</li><li>• Promo materials in athlete bags</li><li>• Option to sponsor a prize</li><li>• One complimentary athlete entry</li></ul>
  </div>
  <div class="pkg" style="left:334px">
    <svg class="chev" width="20" height="16" viewBox="0 0 20 16"><g fill="none" stroke="#D3D3D3" stroke-width="3"><polyline points="2,2 10,7 18,2"/><polyline points="2,8 10,13 18,8"/></g></svg>
    <h3>DELTA SPONSOR<br><span class="price">$250</span><br>(UNLIMITED)</h3>
    <div class="sub">Ideal for businesses seeking local and digital visibility with support from the event.</div>
    <span class="pill">INCLUDES</span>
    <ul><li>• Logo on event banner</li><li>• Group social media thanks</li><li>• Recognition on media and web</li><li>• Promo materials in athlete bags</li><li>• Option to sponsor a prize</li><li>• One complimentary spectator pass</li></ul>
  </div>
  <div class="inkind">
    <svg class="abs" style="left:12px;top:14px" width="22" height="62" viewBox="0 0 22 62"><g fill="none" stroke="#1C1C1C" stroke-width="3"><polyline points="2,2 11,8 20,2"/><polyline points="2,10 11,16 20,10"/><polyline points="2,18 11,24 20,18"/></g><circle cx="11" cy="44" r="8" fill="#1C1C1C"/></svg>
    <h3>IN-KIND SPONSORSHIPS – PRODUCT OR SERVICE DONATIONS</h3>
    <p>We welcome in-kind contributions that enhance the event experience or operations.</p>
    <span class="pill">EXAMPLES</span>
    <ul><li>• Hydration and nutrition (drinks, snacks, supplements)</li><li>• Equipment and accessories (targets, uniforms, gear)</li><li>• Media, printing, or logistics services</li><li>• Transportation, photography, or volunteer support</li></ul>
  </div>
</section>

<!-- DIVISIONS -->
<section class="page divisions" style="left:83px;top:2912px">
  <div class="ghost-num">06</div>
  <h2 class="title" style="left:56px;top:37px">6. EVENT DIVISIONS (UPDATED)</h2>
  <div class="abs" style="left:12px;top:120px;writing-mode:vertical-rl;transform:rotate(180deg);font-size:6px;opacity:.7">DECEMBER 2026 &nbsp; | &nbsp; 8</div>
  <div class="jibaro"></div>
  <div class="dv" style="left:93px;top:88px"><div class="circ alt" role="img" aria-label="Adaptive athlete on course"><span class="badge"></span></div><h4>SCALE DIVISION (<br>ADAPTIVE)</h4><div class="kind">Event Division</div><p>An adaptive division for those who want to experience ITBC in a controlled environment. No rankings. No prizes. This is about completing the challenge.</p></div>
  <div class="dv" style="left:273px;top:88px"><div class="circ" role="img" aria-label="Beginner athlete with pistol"><span class="badge"></span></div><h4>BEGINNER<br>DIVISION</h4><div class="kind">Event Division</div><p>For athletes ready to compete in a structured and approachable format. Challenging, but accessible. Athletes compete for placement.</p></div>
  <div class="dv" style="left:422px;top:88px"><div class="circ alt" role="img" aria-label="Intermediate athlete shooting"><span class="badge"></span></div><h4>INTERMEDIATE<br>DIVISION</h4><div class="kind">Event Division</div><p>For athletes with a strong foundation in fitness and shooting. Heavier loads. Higher standards. Performance matters.</p></div>
  <div class="dv elite" style="left:103px;top:376px"><div class="circ" style="border-color:var(--charcoal)" role="img" aria-label="Elite athlete with rifle"><span class="badge"></span></div><h4>JÍBARO DIVISION</h4><div class="kind">(Elite)</div><p>The highest level of competition at ITBC. Retention holsters required. Rifles carried in slings. Heavier loads. Built for athletes who want to prove themselves.</p></div>
  <div class="dv" style="left:273px;top:376px"><div class="circ alt" role="img" aria-label="Masters athlete aiming"><span class="badge"></span></div><h4>MASTERS 45+<br>DIVISION</h4><div class="kind">Event Division</div><p>For athletes 45+ who want to compete while prioritizing longevity and control. Maintains competitive intensity within an age-based category.</p></div>
  <div class="dv" style="left:422px;top:376px"><div class="circ" role="img" aria-label="Athlete transitioning between rifle and pistol"><span class="badge"></span></div><h4>2-GUN<br>FORMAT</h4><div class="kind">(IMPORTANT – INCLUDE)</div><p>All divisions are available in either:<br>Pistol<br>2-Gun (Pistol + Rifle)<br><br>In the 2-Gun format, athletes utilize both pistol and rifle throughout the competition, transitioning between weapons under physical fatigue and time pressure.</p></div>
</section>

<!-- EXPECTED ATTENDANCE -->
<section class="page expected" style="left:619px;top:2912px">
  <div class="tag" style="right:30px;top:28px">Sponsorship Proposal 2026</div>
  <div class="side" style="top:120px">SPONSORSHIP PROPOSAL &nbsp; | &nbsp; 9</div>
  <div class="photo portrait" style="left:46px;top:51px;width:251px;height:631px" role="img" aria-label="Athlete in cap and sunglasses carrying a rifle on the range"></div>
  <div class="exp" style="top:84px;font-size:8px">The Iron Trials Borinquen<br>Coast<br><span style="font-size:6px;opacity:.7">ITBC</span></div>
  <div class="exp" style="top:150px;font-family:var(--head);font-size:46px;color:var(--sand);line-height:1">”</div>
  <div class="exp" style="top:212px">
    <h3>EXPECTED<br>ATTENDANCE:</h3>
    <ul style="margin-top:18px">
      <li>130+ athletes</li><li>300+ spectators</li><li>500 total attendees</li>
      <li style="margin-top:6px">Theme: Christmas<br>Experience</li>
      <li style="margin-top:6px">Full event decorated<br>in Christmas theme</li>
      <li style="margin-top:6px">Full event decorated<br>in Christmas theme</li>
    </ul>
  </div>
  <div class="exp" style="top:462px;font-size:16px;line-height:1.15">December<br>19, 2026</div>
  <div class="exp" style="top:516px;font-size:6px;line-height:1.4">This is NOT just a competition -<br>it is an experience-driven event.</div>
  <div class="exp" style="top:612px;font-size:10px">~500 <span style="font-size:6px">total attendees</span></div>
</section>

<!-- CONTACT -->
<section class="page contact" style="left:76px;top:3624px">
  <div class="photo range" style="left:0;top:0;width:528px;height:560px" role="img" aria-label="Athletes training and shooting on the range"></div>
  <svg class="abs" style="left:0;top:0" width="528" height="682" viewBox="0 0 528 682" aria-hidden="true">
    <path d="M0 520 L0 682 L528 682 L528 520 L420 520 A161 161 0 0 1 106 520Z" fill="#1C1C1C"/>
    <circle cx="263" cy="436" r="161" fill="none" stroke="#1C1C1C" stroke-width="24"/>
  </svg>
  <div class="logo-badge" style="left:165px;top:338px;width:196px;height:196px;font-size:36px">ITBC</div>
  <div class="band" style="left:0;top:563px;width:195px;height:34px;font-size:15px">CONTACT</div>
  <div class="cover-meta" style="left:30px;top:628px;text-align:left;font-size:6px">Ridgeline Range Club<br>Cerro Alto,<br>Puerto Rico</div>
  <div class="cover-meta" style="left:160px;top:662px;font-size:6px;text-align:left">Email: rafael@theitbc-example.com | Phone: 555-014-0199</div>
  <div class="cover-meta" style="right:30px;top:658px;font-size:8px">www.instagram.com/theitbc_demo</div>
</section>

</body>
</html>
```